Dermal Care Nursing Circle - Rack Card Design

This is a 2-sided rack card that should be 3.5 inches wide by 8.5 inches tall.

Text (with instructions), logo and website image are attached. For the main image on the front, you can use the attached image, or pull whatever you like off of brightstockpix.example, and we will purchase the photo from the winning design

The front should have text plus a nurse image, the back should have mostly text with the website image and legend.
Updates

We have received many high quality designs, but it is apparent to us that at the print size we are currently using (3.5x8.5), that the image of the homepage on the back is too small, and not legible. As such, we have decided that we would like to go with a horizontal version at 8.5 wide by 5.5 tall, with a larger more legible version of the website on the back and call outs to one side or the other, please resubmit your designs in that format. Thank you, and sorry for the inconvenience. Ray

Industry/Entity Type

Nurse

Font styles to use
Sans Serif

Colors
876aae
6b449b
b7a5cd
e4daeb

Requirements
Must have
• Please use the color palate from the attached logo, and a nursing image on the front.

```html
<!DOCTYPE html>
<html lang="en">
<head>
<meta charset="utf-8">
<title>Dermal Care Nursing Circle – Rack Card</title>
<link href="https://fonts.googleapis.com/css2?family=Montserrat:wght@400;600;700&family=Cabin:wght@600&family=Roboto+Condensed:wght@400;700&display=swap" rel="stylesheet">
<style>
:root{
  --purple-deep:#6b449b;
  --purple:#876aae;
  --purple-soft:#b7a5cd;
  --purple-mist:#e4daeb;
  --ink:#222;
  --text:#333;
  --paper:#f4f3f5;
  --stage:#ebe8ee;
  --rule:#d6d0dc;
}
*{margin:0;padding:0;box-sizing:border-box}
html,body{width:1200px;height:1200px;overflow:hidden;background:var(--stage)}
.canvas{position:relative;width:1200px;height:1200px}
.card{position:absolute;left:160px;width:880px;height:570px;background:var(--paper);overflow:hidden;box-shadow:0 4px 14px rgba(0,0,0,.18)}
.card--front{top:20px}
.card--back{top:610px}
.card svg.bg{position:absolute;inset:0}
.abs{position:absolute}

/* front */
.tagline{left:470px;width:390px;top:130px;text-align:center;font-family:Montserrat,sans-serif;color:var(--purple-deep)}
.tagline .big{font-size:34px;font-weight:700;line-height:44px}
.tagline .caps{font-size:21px;font-weight:600;color:#3a3a3a;letter-spacing:.5px;line-height:34px}
.brand{left:470px;width:390px;top:350px;display:flex;justify-content:center;align-items:center;gap:12px;font-family:Montserrat,sans-serif;font-weight:700;font-size:24px;color:var(--purple-deep)}
.brand .dot{width:16px;height:16px;border-radius:50%;background:var(--purple-deep)}
.footer-url{left:40px;top:533px;font-family:Montserrat,sans-serif;font-size:17px;color:#fff;letter-spacing:.3px}

/* back */
.lead{left:24px;width:440px;top:352px;text-align:center;font-family:Cabin,sans-serif;font-weight:600;font-size:19px;line-height:24px;color:var(--ink)}
.lead .cta{display:block;margin-top:6px}
.lead .url{display:block;margin-top:2px;color:var(--purple-deep);letter-spacing:2px}
.feature{position:absolute;text-align:center;font-family:"Roboto Condensed",sans-serif;color:var(--text)}
.feature svg{display:block;margin:0 auto 4px}
.feature h3{font-size:15px;font-weight:700;color:var(--purple-deep);margin-bottom:2px}
.feature p{font-size:12px;line-height:14.5px}
.feature--wide{left:490px;width:370px;top:18px}
.col-l{left:490px;width:180px}
.col-r{left:680px;width:180px}
.divider{left:675px;top:130px;width:1px;height:380px;background:var(--rule)}
</style>
</head>
<body>
<main class="canvas">

  <section class="card card--front" aria-label="Front side">
    <svg class="bg" width="880" height="570" viewBox="0 0 880 570">
      <defs>
        <linearGradient id="photoTone" x1="0" y1="0" x2="0" y2="1">
          <stop offset="0" stop-color="#d9cfe3"/>
          <stop offset=".5" stop-color="#8fa3cf"/>
          <stop offset="1" stop-color="#5f6f9e"/>
        </linearGradient>
        <linearGradient id="greyBand" x1="0" y1="0" x2="1" y2="0">
          <stop offset="0" stop-color="#777"/><stop offset="1" stop-color="#c8c8c8"/>
        </linearGradient>
      </defs>
      <rect width="880" height="570" fill="var(--paper)"/>
      <path d="M0 0H400C470 120 470 380 380 520H0Z" fill="url(#photoTone)" role="img" aria-label="Photo of a smiling nurse in blue scrubs with a stethoscope, arms crossed"/>
      <path d="M400 0H418C488 120 488 380 398 520H380C470 380 470 120 400 0Z" fill="var(--purple-deep)"/>
      <path d="M418 0H440C510 120 510 380 420 520H398C488 380 488 120 418 0Z" fill="url(#greyBand)"/>
      <rect y="520" width="880" height="50" fill="var(--purple-deep)"/>
      <path d="M700 570L880 480V570Z" fill="url(#greyBand)"/>
      <path d="M660 570L880 460V474L690 570Z" fill="var(--purple)"/>
    </svg>
    <div class="abs tagline">
      <div class="big">Inspired by patients</div>
      <div class="caps">EMPOWERED BY KNOWLEDGE</div>
      <div class="big">Impacting melanoma</div>
    </div>
    <div class="abs brand"><span class="dot"></span>Dermal Care Nursing Circle</div>
    <div class="abs footer-url">www.DermalCareCircle.example</div>
  </section>

  <section class="card card--back" aria-label="Back side">
    <svg class="bg" width="880" height="570" viewBox="0 0 880 570">
      <defs>
        <linearGradient id="greyBand2" x1="0" y1="0" x2="1" y2="0">
          <stop offset="0" stop-color="#777"/><stop offset="1" stop-color="#c8c8c8"/>
        </linearGradient>
      </defs>
      <rect width="880" height="570" fill="var(--paper)"/>
      <path d="M0 0H470V180C380 120 200 100 0 110Z" fill="var(--purple-mist)"/>
      <rect x="34" y="22" width="420" height="316" rx="6" fill="#4b2f78" role="img" aria-label="Screenshot of the Dermal Care Nursing Circle website home page"/>
      <rect x="34" y="22" width="420" height="24" rx="6" fill="#fff"/>
      <rect x="34" y="40" width="420" height="110" fill="#f5f5f5"/>
      <rect x="46" y="56" width="190" height="84" fill="#8fa3cf"/>
      <rect x="260" y="60" width="70" height="10" fill="var(--purple)"/>
      <rect x="260" y="80" width="70" height="10" fill="var(--purple)"/>
      <rect x="260" y="100" width="70" height="10" fill="var(--purple)"/>
      <line x1="194" y1="150" x2="194" y2="320" stroke="#6a55a0"/>
      <line x1="314" y1="150" x2="314" y2="320" stroke="#6a55a0"/>
      <rect x="34" y="320" width="420" height="18" fill="#3a2360"/>
      <rect y="520" width="880" height="50" fill="var(--purple-deep)"/>
      <path d="M700 570L880 480V570Z" fill="url(#greyBand2)"/>
      <path d="M660 570L880 460V474L690 570Z" fill="var(--purple)"/>
    </svg>

    <div class="abs lead">
      You wear many hats and take care of patients with many different tumor types.
      <span class="cta">Check out for free access to:</span>
      <span class="url">www.DermalCareCircle.example</span>
    </div>

    <div class="feature feature--wide">
      <svg width="36" height="40" viewBox="0 0 48 52"><path d="M24 2 45 14V38L24 50 3 38V14Z" fill="var(--purple-deep)"/><rect x="16" y="14" width="16" height="22" rx="2" fill="none" stroke="#fff" stroke-width="2.5"/><line x1="20" y1="14" x2="20" y2="36" stroke="#fff" stroke-width="2"/></svg>
      <h3>Nursing Consensus Statements from JCSN</h3>
      <p>Hot off the press! Articles from the Journal of Clinical Skin Nursing outlining practical strategies to manage side-effects and promote adherence to melanoma therapies</p>
    </div>

    <div class="abs divider"></div>

    <div class="feature col-l" style="top:135px">
      <svg width="36" height="40" viewBox="0 0 48 52"><path d="M24 2 45 14V38L24 50 3 38V14Z" fill="var(--purple-deep)"/><rect x="15" y="14" width="18" height="22" fill="none" stroke="#fff" stroke-width="2"/><path d="M18 20h12M18 25h12M18 30h12" stroke="#fff" stroke-width="2"/></svg>
      <h3>Nurse Toolkit</h3>
      <p>Visual and text-based therapeutic side effect management tools</p>
    </div>
    <div class="feature col-r" style="top:135px">
      <svg width="36" height="40" viewBox="0 0 48 52"><path d="M24 2 45 14V38L24 50 3 38V14Z" fill="var(--purple-deep)"/><rect x="14" y="18" width="20" height="16" rx="3" fill="#fff"/><path d="M24 21v10M19 26h10" stroke="var(--purple-deep)" stroke-width="2.5"/></svg>
      <h3>Nurse Toolkit</h3>
      <p>A Nurse's Toolkit with extensive melanoma nursing care resources</p>
    </div>

    <div class="feature col-l" style="top:260px">
      <svg width="36" height="40" viewBox="0 0 48 52"><path d="M24 2 45 14V38L24 50 3 38V14Z" fill="var(--purple-deep)"/><rect x="16" y="14" width="16" height="22" rx="2" fill="none" stroke="#fff" stroke-width="2"/><path d="M24 20v9M20 25l4 4 4-4" stroke="#fff" stroke-width="2" fill="none"/></svg>
      <h3>Printable Patient Materials</h3>
      <p>Printable patient resources to provide patients, organized by therapy</p>
    </div>
    <div class="feature col-r" style="top:260px">
      <svg width="36" height="40" viewBox="0 0 48 52"><path d="M24 2 45 14V38L24 50 3 38V14Z" fill="var(--purple-deep)"/><path d="M12 16h24v15H22l-6 5v-5h-4Z" fill="#fff"/><circle cx="21" cy="22" r="2.5" fill="var(--purple-deep)"/><circle cx="28" cy="22" r="2.5" fill="var(--purple-deep)"/></svg>
      <h3>Q &amp; A Community</h3>
      <p>An oncology nurse community forum to share successes, challenges, insights, and solutions</p>
    </div>

    <div class="feature col-l" style="top:395px">
      <svg width="36" height="40" viewBox="0 0 48 52"><path d="M24 2 45 14V38L24 50 3 38V14Z" fill="var(--purple-deep)"/><circle cx="19" cy="30" r="5" fill="none" stroke="#fff" stroke-width="2.5"/><path d="M22 27 32 17" stroke="#fff" stroke-width="2.5"/></svg>
      <h3>Education</h3>
      <p>Online educational modules, newsfeeds, and other material to keep you up to date</p>
    </div>
    <div class="feature col-r" style="top:395px">
      <svg width="36" height="40" viewBox="0 0 48 52"><path d="M24 2 45 14V38L24 50 3 38V14Z" fill="var(--purple-deep)"/><rect x="13" y="16" width="22" height="18" rx="2" fill="none" stroke="#fff" stroke-width="2"/><rect x="16" y="20" width="6" height="6" fill="#fff"/><path d="M25 21h7M25 25h7M16 30h16" stroke="#fff" stroke-width="2"/></svg>
      <h3>NEWS</h3>
      <p>And much more!</p>
    </div>

    <div class="abs footer-url">www.DermalCareCircle.example</div>
  </section>

</main>
</body>
</html>
```